Business Card for Bloom Vitality & Strength

Hi can you please design a business card with my logo and program logo (the new one I just sent) somewhere on it too maybe on the back? Needs to be eye catching and super cool.
Trudy Melcombe, Director
Master Personal Trainer & Nutrition Coach
0472 816 305
Www.bloomvitalitystrength.com.au
Insta (logo) bloom_vitality_strength #bloomyou7x72018

Target Market(s)

30+ women looking to change lifestyle to healthy mind body etc

Industry/Entity Type

Health And Wellness

Contact Information for Business Card

As above

Font styles to use
Sans Serif

Colors

Designer to choose colors to be used in the design.

Requirements
Must have
• Must super cool and edgy with a bit of cuteness

```html
<!DOCTYPE html>
<html lang="en">
<head>
<meta charset="utf-8">
<title>Bloom Vitality &amp; Strength – Business Card</title>
<link href="https://fonts.googleapis.com/css2?family=Lato:wght@400;700;900&display=swap" rel="stylesheet">
<style>
  :root {
    --backdrop: #ece9e6;
    --card: #ffffff;
    --red: #c8000a;
    --red-deep: #a50008;
    --red-bright: #e3121b;
    --ink: #111111;
    --card-shadow: rgba(0, 0, 0, 0.18);
  }
  * { margin: 0; padding: 0; box-sizing: border-box; }
  html, body {
    width: 1200px;
    height: 900px;
    overflow: hidden;
    background: var(--backdrop);
    font-family: "Lato", sans-serif;
  }
  .stage { position: relative; width: 1200px; height: 900px; }

  .card {
    position: absolute;
    background: var(--card);
    box-shadow: 0 6px 22px var(--card-shadow);
    overflow: hidden;
  }

  /* Front */
  .card-front { left: 178px; top: 75px; width: 588px; height: 363px; }
  .accent-shape { position: absolute; left: 0; top: 0; width: 290px; height: 363px; }

  .identity {
    position: absolute;
    right: 36px;
    top: 44px;
    text-align: right;
    color: var(--ink);
  }
  .identity .name {
    color: var(--red);
    font-weight: 700;
    font-size: 21px;
    letter-spacing: 0.5px;
    line-height: 1.2;
  }
  .identity .role { font-size: 16px; line-height: 1.4; }

  .contact-list {
    position: absolute;
    right: 36px;
    top: 246px;
    list-style: none;
    text-align: right;
    font-size: 16px;
    color: var(--ink);
  }
  .contact-list li {
    display: flex;
    justify-content: flex-end;
    align-items: center;
    gap: 3px;
    line-height: 23px;
  }
  .contact-list li.social { margin-top: 10px; }
  .contact-icon { width: 14px; height: 14px; flex: none; }

  /* Back */
  .card-back { left: 388px; top: 505px; width: 567px; height: 352px; }
  .brand-mark, .program-mark {
    position: absolute;
    left: 0;
    width: 100%;
    display: flex;
    justify-content: center;
    align-items: center;
    gap: 10px;
    color: var(--ink);
    font-weight: 900;
  }
  .brand-mark { top: 92px; font-size: 27px; letter-spacing: 0.5px; }
  .program-mark { top: 220px; font-size: 25px; font-weight: 400; letter-spacing: 2px; }
  .mark-dot {
    width: 16px;
    height: 16px;
    border-radius: 50%;
    background: var(--red);
    flex: none;
  }
</style>
</head>
<body>
<main class="stage">

  <section class="card card-front" aria-label="Business card front">
    <svg class="accent-shape" viewBox="0 0 290 363" role="img" aria-label="Red decorative accent panel">
      <defs>
        <radialGradient id="accentGlow" cx="0.4" cy="0.5" r="0.75">
          <stop offset="0" stop-color="var(--red-bright)"/>
          <stop offset="1" stop-color="var(--red-deep)"/>
        </radialGradient>
      </defs>
      <path d="M0 0 H170 C250 80 285 170 270 250 C255 315 180 345 0 363 Z" fill="url(#accentGlow)"/>
    </svg>

    <div class="identity">
      <p class="name">TRUDY MELCOMBE</p>
      <p class="role">Director</p>
      <p class="role">Master Personal Trainer &amp; Nutrition Coach</p>
    </div>

    <ul class="contact-list">
      <li>0472 816 305
        <svg class="contact-icon" viewBox="0 0 14 14" aria-hidden="true">
          <path d="M2 4 C2 2 12 2 12 4 L11 6 L9 5.3 L9 4.3 C8 4 6 4 5 4.3 L5 5.3 L3 6 Z" fill="var(--red)"/>
          <rect x="3" y="7" width="8" height="5" rx="1" fill="var(--red)"/>
        </svg>
      </li>
      <li>www.bloomvitalitystrength.com.au
        <svg class="contact-icon" viewBox="0 0 14 14" aria-hidden="true">
          <circle cx="7" cy="7" r="6" fill="var(--red)"/>
          <path d="M1.5 7 H12.5 M7 1 C4 4 4 10 7 13 M7 1 C10 4 10 10 7 13" stroke="#fff" stroke-width="0.9" fill="none"/>
        </svg>
      </li>
      <li class="social">bloom_vitality_strength #bloomyou7x72018
        <svg class="contact-icon" viewBox="0 0 14 14" aria-hidden="true">
          <rect x="1" y="1" width="12" height="12" rx="2" fill="var(--red)"/>
        </svg>
      </li>
    </ul>
  </section>

  <section class="card card-back" aria-label="Business card back">
    <div class="brand-mark">
      <span>BLOOM VITALITY &amp; STRENGTH</span>
      <span class="mark-dot"></span>
    </div>
    <div class="program-mark">
      <span>BloomYou7x7</span>
      <span class="mark-dot"></span>
    </div>
  </section>

</main>
</body>
</html>
```